Book Cover "Venice"

Creation of a cover (14 x 20.5 cm + bleed area) for a book:
Image: “BrumeVerte” (Tiff joined)
AUTHOR: Corinne Valmer
TITLE: The murmurs of Lorient
PUBLISHER: Editions Pluvane (AT THE BOTTOM OF THE COVER)

Target Market(s)

Readers of romantic novels

Industry/Entity Type

Book

```html
<!DOCTYPE html>
<html lang="en">
<head>
<meta charset="utf-8">
<title>The murmurs of Lorient — Book Cover</title>
<link rel="stylesheet" href="https://fonts.googleapis.com/css2?family=Italiana&family=Poppins:wght@300;400&display=swap">
<style>
  :root {
    --backdrop: #e9e9ea;
    --sky-top: #5a1420;
    --sky-upper: #b81d22;
    --sky-mid: #e8321e;
    --sky-glow: #f04a22;
    --sky-low: #c8261c;
    --silhouette: #1a0a0c;
    --ink-light: #ffffff;
    --ink-soft: rgba(255,255,255,0.92);
  }
  * { margin: 0; padding: 0; box-sizing: border-box; }
  html, body {
    width: 1200px; height: 1000px; overflow: hidden;
    background: var(--backdrop);
  }
  .stage {
    position: relative; width: 1200px; height: 1000px;
  }
  .book-cover {
    position: absolute; left: 300px; top: 60px;
    width: 600px; height: 879px; overflow: hidden;
    box-shadow: 6px 8px 14px rgba(0,0,0,0.35);
  }
  .cover-photo {
    position: absolute; inset: 0;
    background:
      radial-gradient(ellipse 70% 30% at 55% 58%, var(--sky-glow) 0%, transparent 70%),
      linear-gradient(180deg,
        var(--sky-top) 0%,
        var(--sky-upper) 14%,
        var(--sky-mid) 40%,
        var(--sky-glow) 58%,
        var(--sky-low) 72%,
        #4a0e10 84%,
        var(--silhouette) 100%);
  }
  .author-block {
    position: absolute; top: 38px; left: 0; right: 0;
    text-align: center; color: var(--ink-light);
    font-family: "Poppins", sans-serif;
  }
  .author-label {
    font-size: 12px; font-weight: 400; letter-spacing: 0.5px;
  }
  .author-name {
    margin-top: 6px; font-size: 18px; font-weight: 400;
    letter-spacing: 5px; text-transform: uppercase;
  }
  .title {
    position: absolute; top: 218px; left: 0; right: 0;
    text-align: center; color: var(--ink-light);
    font-family: "Italiana", serif; font-weight: 400;
    text-shadow: 0 2px 6px rgba(60,0,0,0.35);
    line-height: 1;
  }
  .title-article {
    display: block; font-size: 46px; margin-left: -270px;
  }
  .title-main {
    display: block; font-size: 86px; letter-spacing: -1px; margin-top: -8px;
  }
  .title-place {
    display: block; font-size: 58px; margin-top: 4px;
  }
  .title-place .title-of {
    font-size: 34px; margin-right: 4px;
  }
  .publisher {
    position: absolute; bottom: 30px; left: 0; right: 0;
    text-align: center; color: var(--ink-soft);
    font-family: "Poppins", sans-serif; font-size: 14px; font-weight: 400;
    text-transform: uppercase;
  }
</style>
</head>
<body>
  <main class="stage">
    <article class="book-cover">
      <div class="cover-photo" role="img" aria-label="Photograph: blazing red sunset sky over a silhouetted domed church and ornate glowing street lanterns"></div>

      <header class="author-block">
        <p class="author-label">AUTHOR</p>
        <p class="author-name">Corinne Valmer</p>
      </header>

      <h1 class="title">
        <span class="title-article">The</span>
        <span class="title-main">MURMURS</span>
        <span class="title-place"><span class="title-of">of</span>LORIENT</span>
      </h1>

      <p class="publisher">Publisher – Editions Pluvane</p>
    </article>
  </main>
</body>
</html>
```